Retail Seafood business needs package/label design

In need of packaging/label design for multiple seafood products such as sword fish, halibut, cod fish, scallops, mahi, catfish, and lobster tails

```html
<!DOCTYPE html>
<html lang="en">
<head>
<meta charset="utf-8">
<title>Sword Fish Label</title>
<link href="https://fonts.googleapis.com/css2?family=Roboto+Condensed:wght@700&family=Oswald:wght@500&display=swap" rel="stylesheet">
<style>
  :root {
    --page-bg: #e6e6e6;
    --label-bg: #ededed;
    --label-dark: #3c3c3c;
    --stripe-mid: #9b9b9b;
    --stripe-light: #bdbdbd;
    --ribbon: #8a8a8a;
    --ink-white: #ffffff;
    --ink-dark: #1c1c1c;
    --fish-blue: #4a6a9a;
    --fish-pale: #dfe6ef;
    --fish-gold: #d8a04c;
  }
  html, body {
    margin: 0;
    width: 1200px;
    height: 830px;
    overflow: hidden;
    background: var(--page-bg);
  }
  .stage {
    position: relative;
    width: 1200px;
    height: 830px;
  }
  .label {
    position: absolute;
    left: 360px;
    top: 25px;
    width: 480px;
    height: 780px;
    display: block;
  }
  .title {
    font-family: "Roboto Condensed", "Arial Narrow", sans-serif;
    font-weight: 700;
    font-size: 60px;
    fill: var(--ink-white);
  }
  .badge-text {
    font-family: "Roboto Condensed", "Arial Narrow", sans-serif;
    font-weight: 700;
    font-size: 15px;
    fill: var(--ink-white);
  }
  .tagline {
    font-family: "Oswald", "Arial Narrow", sans-serif;
    font-weight: 500;
    font-size: 15px;
    letter-spacing: 3.5px;
    fill: var(--ink-dark);
  }
</style>
</head>
<body>
<main class="stage">
  <svg class="label" viewBox="0 0 400 650" xmlns="http://www.w3.org/2000/svg">
    <defs>
      <linearGradient id="stripeGrad" x1="0" y1="0" x2="1" y2="0">
        <stop offset="0" stop-color="#6f6f6f"/>
        <stop offset="0.6" stop-color="#a8a8a8"/>
        <stop offset="1" stop-color="#d0d0d0"/>
      </linearGradient>
      <linearGradient id="ribbonGrad" x1="0" y1="0" x2="0" y2="1">
        <stop offset="0" stop-color="#6e6e6e"/>
        <stop offset="1" stop-color="#a9a9a9"/>
      </linearGradient>
      <radialGradient id="fishGrad" cx="0.45" cy="0.45" r="0.6">
        <stop offset="0" stop-color="var(--fish-pale)"/>
        <stop offset="0.55" stop-color="var(--fish-blue)" stop-opacity="0.55"/>
        <stop offset="1" stop-color="var(--fish-gold)" stop-opacity="0"/>
      </radialGradient>
    </defs>

    <rect class="label-base" width="400" height="650" fill="var(--label-bg)"/>

    <path class="dark-panel" d="M0,0 L285,0 C310,90 355,165 400,195 L400,292 C290,296 120,350 0,395 Z" fill="var(--label-dark)"/>
    <path class="top-stripe" d="M285,0 L305,0 C330,85 365,150 400,175 L400,195 C355,165 310,90 285,0 Z" fill="url(#stripeGrad)"/>
    <path class="lower-stripe" d="M0,395 C120,350 290,296 400,292 L400,306 C300,312 140,370 0,440 Z" fill="url(#stripeGrad)"/>
    <path class="lower-stripe-thin" d="M0,448 C140,380 300,322 400,316 L400,322 C300,330 150,392 0,458 Z" fill="var(--stripe-light)"/>

    <g class="fresh-badge">
      <polygon points="292,0 333,22 374,0 374,165 292,165" fill="url(#ribbonGrad)"/>
      <text class="badge-text" x="333" y="155" text-anchor="middle">FRESH</text>
    </g>

    <text class="title" x="48" y="233">Sword</text>
    <text class="title" x="46" y="295">Fish</text>

    <ellipse class="fish-illustration" role="img" aria-label="Illustration of a leaping swordfish" cx="290" cy="330" rx="115" ry="120" fill="url(#fishGrad)"/>

    <text class="tagline" x="200" y="564" text-anchor="middle">AUTHENTIC SEAFOOD</text>
    <text class="tagline" x="200" y="584" text-anchor="middle">STRAIGHT FROM</text>
    <text class="tagline" x="200" y="604" text-anchor="middle">THE OCEAN</text>
  </svg>
</main>
</body>
</html>
```